Lanternwick Pathway Ledger Basics

size of the ad - 8”x 10.75" plus 0.25" bleed
I would like an ad for a magazine that will stand out and make people want to read the ad.
The ad should not be crowded and people reading the ad will be able to read the text.
I would like it to be a creative and modern-day design.
the list of topics should not be the focus of the ad.
the text is attached.
If you decide to use people in the ad then please no ladies.
please note that leave over 1 inch for the bottom of the footer

```html
<!DOCTYPE html>
<html lang="en">
<head>
<meta charset="utf-8">
<title>Real Estate Course – Lanternwick Pathway Ledger Basics</title>
<link href="https://fonts.googleapis.com/css2?family=Arimo:wght@700&family=Fira+Sans:wght@300;400;500;600&display=swap" rel="stylesheet">
<style>
  :root {
    --navy: #0d365d;
    --band-blue: #0a6bb5;
    --bright-blue: #1b8de4;
    --yellow: #fbf43a;
    --white: #ffffff;
    --mist: #e6e7e8;
    --orange: #ef5a2a;
    --ink: #14294a;
    --divider: #a9b0b8;
    --page: #e4e4e4;
  }
  * { box-sizing: border-box; margin: 0; padding: 0; }
  html, body { width: 1200px; height: 1200px; overflow: hidden; }
  body {
    background: var(--page);
    font-family: "Fira Sans", Arial, sans-serif;
    position: relative;
  }
  .ad {
    position: absolute;
    left: 175px; top: 30px;
    width: 849px; height: 1140px;
    background: var(--white);
    overflow: hidden;
  }
  .hero {
    position: absolute; left: 0; top: 0;
    width: 849px; height: 690px;
    background: var(--navy);
  }
  .hero__title {
    position: absolute; left: 0; right: 0; top: 62px;
    text-align: center;
    font-family: "Arimo", Arial, sans-serif;
    font-weight: 700; font-size: 58px; line-height: 1;
    color: var(--yellow);
    white-space: nowrap;
  }
  .hero__subtitle {
    position: absolute; left: 0; right: 0; top: 135px;
    text-align: center;
    font-weight: 600; font-size: 40px; line-height: 1;
    color: var(--bright-blue);
    white-space: nowrap;
  }
  .hero__tagline {
    position: absolute; left: 0; right: 0; top: 186px;
    text-align: center;
    font-weight: 400; font-size: 28px; line-height: 1;
    color: var(--white);
    white-space: nowrap;
  }
  .hero__tagline b { font-weight: 600; }
  .hero__skyline {
    position: absolute; left: 50px; top: 263px;
    width: 745px; height: 427px;
    background: linear-gradient(180deg, rgba(255,255,255,0.55) 0%, rgba(255,255,255,0.85) 100%);
  }
  .details {
    position: absolute; left: 0; top: 690px;
    width: 849px; height: 106px;
    background: var(--band-blue);
  }
  .details__divider, .offers__divider {
    position: absolute; width: 2px;
    background: var(--divider);
  }
  .details__divider { top: 18px; height: 72px; }
  .details__town {
    position: absolute; left: 50px; top: 24px;
    font-weight: 500; font-size: 60px; line-height: 1;
    color: var(--yellow);
    white-space: nowrap;
  }
  .details__sessions {
    position: absolute; left: 351px; top: 18px;
    line-height: 1;
    white-space: nowrap;
  }
  .details__count {
    display: block;
    font-weight: 300; font-size: 42px; color: var(--white);
  }
  .details__evenings {
    display: block; margin-top: 2px;
    font-weight: 600; font-size: 25px; color: var(--yellow);
  }
  .details__start {
    position: absolute; left: 660px; top: 22px; width: 138px;
    text-align: center; line-height: 1;
    white-space: nowrap;
  }
  .details__start-label {
    display: block;
    font-weight: 300; font-size: 29px; color: var(--white);
  }
  .details__start-date {
    display: block; margin-top: 6px;
    font-weight: 600; font-size: 29px; color: var(--yellow);
  }
  .offers {
    position: absolute; left: 0; top: 796px;
    width: 849px; height: 93px;
    background: var(--mist);
  }
  .offers__divider { top: 14px; height: 64px; }
  .offers__item {
    position: absolute; top: 19px;
    font-size: 22px; line-height: 28px; font-weight: 600;
    white-space: nowrap;
  }
  .offers__scholarship { left: 52px; color: var(--orange); }
  .offers__early { left: 292px; color: var(--ink); }
  .offers__early span { font-weight: 500; }
  .offers__audience { left: 467px; color: var(--ink); }
  .topics {
    position: absolute; left: 0; top: 889px;
    width: 849px; height: 251px;
  }
  .topics__heading {
    position: absolute; left: 52px; top: 23px;
    font-weight: 600; font-size: 19px; color: var(--band-blue);
  }
  .topics__list {
    position: absolute; list-style: none;
  }
  .topics__list li {
    display: flex; align-items: center; gap: 7px;
    font-size: 16.5px; color: var(--ink); height: 29px;
    white-space: nowrap;
  }
  .topics__list svg { width: 13px; height: 13px; flex: none; }
  .topics__list--first { left: 52px; top: 52px; }
  .topics__list--second { left: 369px; top: 24px; }
  .topics__list--third { left: 613px; top: 20px; }
  .topics__list--third li { height: 33px; }
</style>
</head>
<body>
  <svg width="0" height="0" style="position:absolute">
    <defs>
      <symbol id="tick" viewBox="0 0 14 14">
        <circle cx="7" cy="7" r="7" fill="#0a6bb5"/>
        <path d="M3.8 7.2 L6.1 9.4 L10.3 4.8" fill="none" stroke="#fff" stroke-width="1.8" stroke-linecap="round" stroke-linejoin="round"/>
      </symbol>
    </defs>
  </svg>

  <main class="ad">
    <section class="hero">
      <h1 class="hero__title">REAL ESTATE COURSE</h1>
      <h2 class="hero__subtitle">LANTERNWICK PATHWAY LEDGER BASICS</h2>
      <p class="hero__tagline">INVESTING IN <b>KNOWLEDGE</b> IS INVESTING IN <b>OPPORTUNITIES</b></p>
      <div class="hero__skyline" role="img" aria-label="White illustration of a commercial city skyline with office towers"></div>
    </section>

    <section class="details">
      <p class="details__town">DORVAN</p>
      <span class="details__divider" style="left:313px"></span>
      <p class="details__sessions">
        <span class="details__count">10 -TUESDAY</span>
        <span class="details__evenings">EVENINGS SESSIONS</span>
      </p>
      <span class="details__divider" style="left:629px"></span>
      <p class="details__start">
        <span class="details__start-label">STARTING</span>
        <span class="details__start-date">FEB.28</span>
      </p>
    </section>

    <section class="offers">
      <p class="offers__item offers__scholarship">LIMITED PARTIAL<br>SCHOLARSHIPS</p>
      <span class="offers__divider" style="left:265px"></span>
      <p class="offers__item offers__early">EARLY BIRD<br><span>SPECIAL</span></p>
      <span class="offers__divider" style="left:440px"></span>
      <p class="offers__item offers__audience">For those that started or<br>would like to go into real estate</p>
    </section>

    <section class="topics">
      <h3 class="topics__heading">TOPICS: PARTIAL LISTING</h3>
      <ul class="topics__list topics__list--first">
        <li><svg><use href="#tick"/></svg>Real estate investment strategies</li>
        <li><svg><use href="#tick"/></svg>Due diligence</li>
        <li><svg><use href="#tick"/></svg>Financing</li>
      </ul>
      <ul class="topics__list topics__list--second">
        <li><svg><use href="#tick"/></svg>Underwriting</li>
        <li><svg><use href="#tick"/></svg>Property management</li>
        <li><svg><use href="#tick"/></svg>Real estate Legal basics</li>
        <li><svg><use href="#tick"/></svg>Sourcing deals</li>
      </ul>
      <ul class="topics__list topics__list--third">
        <li><svg><use href="#tick"/></svg>Syndication</li>
        <li><svg><use href="#tick"/></svg>Dealing with brokers</li>
        <li><svg><use href="#tick"/></svg>Tax fundamentals</li>
      </ul>
    </section>
  </main>
</body>
</html>
```